Business Card Design Project

Need business card for new non profit organization that includes the attached logo in some form.
with this information
Name: Michael Dorrance Pilbeam
Title: President & Founder
A: P.O. Box 51607, Portland, Oregon, 97214-5160
E: mike@dorrancetrust.org
E: mike@mikepilbeam.com
P: 1.971.555.0172

Industry/Entity Type
Non Profit

```html
<!DOCTYPE html>
<html lang="en">
<head>
<meta charset="UTF-8">
<title>Dorrance Trust – Business Card</title>
<link rel="stylesheet" href="https://fonts.googleapis.com/css2?family=Tinos:wght@400&display=swap">
<style>
  :root {
    --page: #ffffff;
    --card: #ffffff;
    --navy: #012469;
    --ink: #222222;
    --band-dark: #1a1a1a;
    --band-light: #bdbcbe;
    --on-navy: #ffffff;
  }
  * { margin: 0; padding: 0; box-sizing: border-box; }
  html, body {
    width: 1200px;
    height: 900px;
    overflow: hidden;
    background: var(--page);
  }
  .canvas {
    position: relative;
    width: 1200px;
    height: 900px;
  }
  .card {
    position: absolute;
    left: 417px;
    top: 130px;
    width: 367px;
    height: 639px;
    background: var(--card);
    box-shadow: 0 0 22px rgba(0, 0, 0, 0.035);
    font-family: "Tinos", "Times New Roman", serif;
    text-align: center;
    overflow: hidden;
  }
  .brand {
    position: absolute;
    top: 130px;
    left: 0;
    width: 100%;
    display: flex;
    align-items: center;
    justify-content: center;
    gap: 12px;
    color: var(--navy);
    font-size: 34px;
    line-height: 1;
  }
  .brand-dot {
    width: 18px;
    height: 18px;
    border-radius: 50%;
    background: var(--navy);
  }
  .holder-name {
    position: absolute;
    top: 273px;
    left: 0;
    width: 100%;
    font-size: 26px;
    color: var(--ink);
    font-weight: 400;
  }
  .role-band {
    position: absolute;
    top: 312px;
    left: 0;
    width: 100%;
    height: 36px;
    line-height: 36px;
    background: linear-gradient(90deg, var(--band-dark) 0%, #6d6d6d 22%, #9a9a9c 50%, var(--band-light) 100%);
    color: var(--on-navy);
    font-size: 20px;
  }
  .contact-panel {
    position: absolute;
    top: 348px;
    left: 0;
    width: 100%;
    height: 291px;
    background: var(--navy);
    color: var(--on-navy);
    font-size: 16px;
    padding-top: 22px;
    list-style: none;
  }
  .contact-panel li {
    height: 34.7px;
    line-height: 22px;
    white-space: nowrap;
  }
</style>
</head>
<body>
  <div class="canvas">
    <article class="card">
      <div class="brand">
        <span class="brand-dot"></span>
        <span class="brand-name">Dorrance Trust</span>
      </div>
      <h1 class="holder-name">Michael Dorrance Pilbeam</h1>
      <div class="role-band">President &amp; Founder</div>
      <ul class="contact-panel">
        <li>A: P.O. Box 51607, Portland, Oregon, 97214-5160</li>
        <li>E: mike@dorrancetrust.org</li>
        <li>E: mike@mikepilbeam.com</li>
        <li>P: 1.971.555.0172</li>
      </ul>
    </article>
  </div>
</body>
</html>
```